Multifamily Investment Strategies

I need a pamphlet or booklet for multifamily commercial real estate investment.

The specific investment vehicle is affordable multifamily apartments. I have uploaded a 5 page pdf detailing my investment strategy.

The target audience for this pamphlet are investors, commercial brokers, and commercial bankers.

I am looking for modern, clean design that is striking and professional but also eye catching.
Updates

I made a few changes to the brief and also corrected two errors.

Target Market(s)

Commercial Real Estate Investors, Brokers, and Bankers

Industry/Entity Type

Real Estate

Font styles to use
Serif

Colors

Designer to choose colors to be used in the design.

Requirements
Must have
• Graphics of or related to apartment buildings.
• My headshot seen on the last page of the pdf
Nice to have
• Imagery related to investment and profits.
Should not have
• The image of an apartment building on the first page of the pdf is just an example. Please don’t use this image.

```html
<!DOCTYPE html>
<html lang="en">
<head>
<meta charset="utf-8">
<title>Multifamily Cashflow Investment Strategy</title>
<link rel="stylesheet" href="https://fonts.googleapis.com/css2?family=Arimo:wght@400&family=Poppins:wght@300&family=Open+Sans:wght@400;600&display=swap">
<style>
  :root {
    --ink: #111111;
    --paper: #ffffff;
    --panel: #ececec;
    --panel-soft: #f2f2f2;
    --magenta: #e5198a;
    --muted: #8a8a8a;
    --backdrop: #e9e3dd;
  }
  * { margin: 0; padding: 0; box-sizing: border-box; }
  html, body { width: 1200px; height: 824px; overflow: hidden; background: var(--backdrop); }
  .spread { position: relative; width: 1200px; height: 824px; display: flex; }
  .page { position: relative; width: 600px; height: 824px; background: var(--paper); }

  /* Left page: About */
  .about-panel {
    position: absolute; left: 48px; top: 48px; right: 48px; bottom: 48px;
    background: linear-gradient(180deg, var(--panel-soft), var(--panel));
  }
  .about-banner {
    position: absolute; left: 132px; top: 318px; width: 340px; height: 72px;
    background: var(--ink);
  }
  .about-title {
    position: absolute; right: 34px; top: 18px;
    font-family: "Poppins", sans-serif; font-weight: 300; font-size: 26px;
    color: var(--paper); letter-spacing: 0.5px;
  }
  .headshot {
    position: absolute; left: 154px; top: 336px; width: 150px; height: 150px;
    background: var(--paper); padding: 6px;
  }
  .headshot-fill {
    width: 100%; height: 100%;
    background: radial-gradient(circle at 50% 40%, #bdbdbd, #5e5e5e 70%, #3a3a3a);
  }
  .intro {
    position: absolute; left: 318px; top: 400px; width: 176px;
    font-family: "Open Sans", sans-serif; font-size: 9.5px; line-height: 1.55; color: var(--ink);
  }
  .intro .name { color: var(--magenta); }
  .bio {
    position: absolute; left: 154px; top: 500px; width: 330px;
    font-family: "Open Sans", sans-serif; font-size: 9.5px; line-height: 1.55; color: var(--ink);
  }

  /* Right page: Cover */
  .cover-title {
    position: absolute; left: 58px; top: 86px;
    font-family: "Arimo", sans-serif; font-size: 18px; line-height: 1.05; letter-spacing: 0.3px;
  }
  .cover-title .line-1 { display: block; color: var(--ink); }
  .cover-title .line-2 { display: block; color: var(--magenta); }
  .backing {
    position: absolute; left: 330px; top: 170px; width: 240px; height: 380px;
    background: var(--panel-soft);
  }
  .hero-art {
    position: absolute; left: 96px; top: 266px; width: 504px; height: 270px;
    background: linear-gradient(160deg, #cfd6de 0%, #c8713f 35%, #a9aeb6 60%, #b7582e 80%, #6d7a63 100%);
  }
  .tagline-box {
    position: absolute; left: 118px; top: 150px; width: 258px; height: 128px;
    background: var(--ink); display: flex; align-items: center; justify-content: center;
  }
  .tagline {
    font-family: "Poppins", sans-serif; font-weight: 300; font-size: 16.5px; line-height: 1.25;
    color: var(--paper); text-align: center;
  }
  .cover-credit {
    position: absolute; left: 0; right: 0; top: 636px; text-align: center;
    font-family: "Arimo", sans-serif; font-size: 10px; color: var(--muted);
  }
  .gutter {
    position: absolute; left: 596px; top: 0; width: 8px; height: 824px;
    background: linear-gradient(90deg, rgba(0,0,0,0), rgba(0,0,0,0.06), rgba(0,0,0,0));
  }
</style>
</head>
<body>
<main class="spread">
  <section class="page page-about">
    <div class="about-panel"></div>
    <div class="about-banner"><h2 class="about-title">About me</h2></div>
    <div class="headshot"><div class="headshot-fill" role="img" aria-label="Headshot portrait of the investor"></div></div>
    <p class="intro"><span class="name">Dana Whitfield</span> is a residential real estate investor and physician with a passion for identifying and fixing problems through innovative and creative solutions.</p>
    <p class="bio">Her transition into commercial real estate is merely an extension of that passion. It is her professional experience in a demanding and competitive field, along with her tenacity and discipline for doing things effectively and efficiently, which instills confidence in her success as a CRE investor.</p>
  </section>

  <section class="page page-cover">
    <h1 class="cover-title"><span class="line-1">MULTIFAMILY CASHFLOW</span><span class="line-2">INVESTMENT STRATEGY</span></h1>
    <div class="backing"></div>
    <div class="hero-art" role="img" aria-label="Illustration of a modern multifamily apartment building with street, trees and cars"></div>
    <div class="tagline-box"><p class="tagline">Turning Underperforming<br>Multifamily Properties<br>into Highly Profitable,<br>Cash Flowing Assets.</p></div>
    <p class="cover-credit">Dana Whitfield, Residential Real Estate Investor.</p>
  </section>
  <div class="gutter"></div>
</main>
</body>
</html>
```